Coconut Chips label

We need a new label design for our food product -- Coconut Chips. Attached is the design of our current label. Please come up with a new design but keep all text information and logos currently on the label. We only need a fresh lay-out, all logos and text information should be retained. Size of the label is 4.7" X 7" inches (w xh).

Thanks for joining and we look forward to seeing your designs!

```html
<!DOCTYPE html>
<html lang="en">
<head>
<meta charset="utf-8">
<title>Coconut Chips Label</title>
<link rel="stylesheet" href="https://fonts.googleapis.com/css2?family=Oswald:wght@300;400;500;600&family=Roboto+Condensed:wght@300;400;500&family=Luckiest+Guy&family=Roboto:wght@500;700&display=swap">
<style>
  :root {
    --sky-glow: #9fe3d4;
    --teal-light: #6cc9bd;
    --teal: #2a8a8f;
    --navy: #123246;
    --deep: #07141c;
    --leaf: #1d4a2b;
    --leaf-light: #3f7a3e;
    --chip: #c07a43;
    --chip-dark: #7b4423;
    --meat: #f1ede2;
    --outline: #c8873a;
    --cream: #f4efe6;
    --panel-line: #6b4a2a;
    --panel-text: #5a3a1e;
    --panel-bg: rgba(235, 228, 214, 0.6);
    --white: #ffffff;
    --label-grey: #ddd6cc;
    --badge-green: #2e8b3e;
    --badge-lime: #7cc242;
  }
  * { margin: 0; padding: 0; box-sizing: border-box; }
  html, body { width: 806px; height: 1200px; overflow: hidden; background: var(--deep); }
  .label {
    position: relative;
    width: 806px;
    height: 1200px;
    overflow: hidden;
    font-family: "Roboto Condensed", sans-serif;
  }
  .scene-art {
    position: absolute; inset: 0;
    background:
      radial-gradient(ellipse 70px 75px at 320px 735px, var(--meat) 0%, rgba(241,237,226,0.7) 55%, transparent 100%),
      radial-gradient(ellipse 60px 70px at 560px 755px, var(--meat) 0%, rgba(241,237,226,0.6) 55%, transparent 100%),
      radial-gradient(ellipse 80px 80px at 540px 410px, rgba(241,237,226,0.9) 0%, rgba(241,237,226,0.4) 55%, transparent 100%),
      radial-gradient(ellipse 260px 190px at 420px 760px, rgba(192,122,67,0.95) 0%, rgba(160,95,50,0.75) 50%, transparent 100%),
      radial-gradient(ellipse 90px 260px at 760px 560px, rgba(192,122,67,0.7) 0%, transparent 100%),
      radial-gradient(ellipse 90px 120px at 30px 700px, rgba(192,122,67,0.6) 0%, transparent 100%),
      radial-gradient(ellipse 150px 200px at 0px 80px, var(--leaf) 0%, rgba(29,74,43,0.6) 60%, transparent 100%),
      radial-gradient(ellipse 170px 210px at 806px 60px, var(--leaf) 0%, rgba(29,74,43,0.6) 60%, transparent 100%),
      radial-gradient(ellipse 160px 120px at 760px 920px, rgba(63,122,62,0.8) 0%, transparent 100%),
      radial-gradient(ellipse 330px 300px at 420px 330px, var(--sky-glow) 0%, var(--teal-light) 30%, var(--teal) 60%, transparent 100%),
      linear-gradient(180deg, var(--leaf) 0%, var(--navy) 40%, var(--navy) 70%, var(--deep) 100%);
  }
  .brand {
    position: absolute;
    left: 292px; top: 26px;
    width: 223px; height: 166px;
    border-radius: 50%;
    background: linear-gradient(180deg, #d9f0f7 0%, var(--cream) 60%, #bfe0a8 100%);
    border: 6px solid #2d6b2a;
    display: flex; align-items: center; justify-content: center;
  }
  .brand-name {
    font-family: "Oswald", sans-serif;
    font-weight: 500;
    font-size: 26px;
    letter-spacing: 4px;
    color: var(--badge-green);
    text-transform: uppercase;
  }
  .title { position: absolute; left: 0; top: 0; width: 806px; height: 800px; overflow: visible; }
  .title text {
    font-family: "Luckiest Guy", "Bowlby One", sans-serif;
    fill: var(--white);
    stroke: var(--outline);
    stroke-width: 9px;
    stroke-linejoin: round;
    paint-order: stroke fill;
  }
  .title .shade { fill: var(--chip-dark); stroke: var(--chip-dark); opacity: 0.55; }

  .claims { position: absolute; left: 23px; top: 869px; display: flex; gap: 6px; align-items: flex-start; }
  .claim { width: 62px; display: flex; flex-direction: column; align-items: center; }
  .claim-label { font-family: "Roboto", sans-serif; font-weight: 700; font-size: 6px; color: var(--white); margin-top: 4px; white-space: nowrap; }

  .maker { position: absolute; left: 33px; top: 990px; color: var(--label-grey); }
  .licence { font-family: "Oswald", sans-serif; font-weight: 600; font-size: 28px; line-height: 1.1; }
  .maker-intro { font-family: "Oswald", sans-serif; font-weight: 300; font-size: 21px; line-height: 1.2; }
  .maker-company { font-family: "Oswald", sans-serif; font-weight: 600; font-size: 23px; line-height: 1.2; text-transform: uppercase; }
  .maker-address { font-family: "Oswald", sans-serif; font-weight: 300; font-size: 19.5px; line-height: 1.3; }
  .code-space { position: absolute; left: 29px; top: 1110px; width: 295px; height: 75px; background: var(--white); }

  .cert { position: absolute; }
  .cert-haccp { left: 369px; top: 978px; }
  .cert-gmp { left: 366px; top: 1106px; }

  .facts {
    position: absolute; left: 523px; top: 795px; width: 266px;
    background: var(--panel-bg);
    border: 2px solid var(--panel-line);
    color: var(--panel-text);
  }
  .facts-head { padding: 2px 6px 3px; border-bottom: 3px solid var(--panel-line); }
  .facts-title { font-family: "Oswald", sans-serif; font-weight: 500; font-size: 17px; line-height: 1.2; }
  .facts-serving { font-weight: 300; font-size: 12.5px; line-height: 1.2; }
  .facts table { width: 100%; border-collapse: collapse; font-size: 11px; }
  .facts td { border-top: 1px solid var(--panel-line); padding: 0 5px; height: 16.6px; }
  .facts td.rdi { width: 64px; border-left: 1px solid var(--panel-line); text-align: center; }
  .facts .row-container td { font-weight: 300; font-size: 12.5px; height: 23px; }
  .facts .row-amount td { font-weight: 500; font-size: 12.5px; height: 23px; }
  .facts .row-amount td.rdi { font-weight: 300; font-size: 11px; }
  .facts .row-cal td { height: 22px; }
  .facts b { font-weight: 500; }
  .facts .sub { padding-left: 13px; font-weight: 300; }
  .facts .light { font-weight: 300; }
  .facts-note { border-top: 1px solid var(--panel-line); padding: 4px 5px; font-size: 8px; font-weight: 300; line-height: 1.35; }

  .ingredients { position: absolute; left: 524px; top: 1101px; color: var(--white); font-family: "Oswald", sans-serif; }
  .ingredients-title { font-weight: 500; font-size: 15px; line-height: 1.2; }
  .ingredients-list { font-weight: 300; font-size: 14px; line-height: 1.2; }
  .net-weight { position: absolute; left: 553px; top: 1146px; font-family: "Roboto", sans-serif; font-weight: 700; font-size: 26px; color: var(--white); }
</style>
</head>
<body>
<main class="label">
  <div class="scene-art" role="img" aria-label="Illustration of tropical palm leaves and cracked coconut halves with flying toasted coconut chips against a teal sky"></div>

  <div class="brand"><span class="brand-name">Isla Grove</span></div>

  <h1>
    <svg class="title" viewBox="0 0 806 800" aria-label="Coconut Chips">
      <g transform="translate(72 535) rotate(-24)">
        <text class="shade" x="5" y="5" font-size="200" textLength="665" lengthAdjust="spacingAndGlyphs">COCONUT</text>
        <text x="0" y="0" font-size="200" textLength="665" lengthAdjust="spacingAndGlyphs">COCONUT</text>
      </g>
      <g transform="translate(140 712) rotate(-33)">
        <text class="shade" x="5" y="5" font-size="165" textLength="450" lengthAdjust="spacingAndGlyphs">CHIPS</text>
        <text x="0" y="0" font-size="165" textLength="450" lengthAdjust="spacingAndGlyphs">CHIPS</text>
      </g>
    </svg>
  </h1>

  <div class="claims">
    <div class="claim">
      <svg width="60" height="60" viewBox="0 0 60 60"><circle cx="30" cy="30" r="27" fill="none" stroke="#fff" stroke-width="3"/></svg>
      <span class="claim-label">GLUTEN FREE</span>
    </div>
    <div class="claim">
      <svg width="60" height="60" viewBox="0 0 60 60"><circle cx="30" cy="30" r="27" fill="none" stroke="#fff" stroke-width="3"/></svg>
      <span class="claim-label">100% VEGETARIAN</span>
    </div>
    <div class="claim">
      <svg width="70" height="66" viewBox="0 0 70 66"><circle cx="35" cy="33" r="24" fill="#fff"/></svg>
    </div>
  </div>

  <section class="maker">
    <p class="licence">FDO LTO-30001234567</p>
    <p class="maker-intro">Manafacrured by:</p>
    <p class="maker-company">Aze Solutan Foods Inc.</p>
    <p class="maker-address">Marlo Street, Danao, Bohol, 6300 Philippines</p>
  </section>
  <div class="code-space"></div>

  <svg class="cert cert-haccp" width="106" height="106" viewBox="0 0 106 106">
    <circle cx="53" cy="53" r="51" fill="#fff"/>
    <circle cx="53" cy="53" r="45" fill="var(--badge-green)"/>
    <circle cx="53" cy="53" r="31" fill="#fff"/>
  </svg>
  <svg class="cert cert-gmp" width="100" height="78" viewBox="0 0 100 78">
    <path d="M50 4 A46 46 0 0 1 96 50 L96 78 L4 78 L4 50 A46 46 0 0 1 50 4 Z" fill="#fff"/>
    <path d="M50 13 A37 37 0 0 1 87 50 L87 70 L13 70 L13 50 A37 37 0 0 1 50 13 Z" fill="var(--badge-lime)"/>
  </svg>

  <section class="facts">
    <div class="facts-head">
      <h2 class="facts-title">NUTRITION FACTS</h2>
      <p class="facts-serving">Serving Size 30 grams</p>
    </div>
    <table>
      <tr class="row-container"><td colspan="2">Serving per Container About 8</td></tr>
      <tr class="row-amount"><td>Amount per Serving</td><td class="rdi">%RENI*</td></tr>
      <tr class="row-cal"><td><b>Calories (kcal)</b> <span class="light">169</span> <b>Calories from Fat</b> <span class="light">98</span></td><td class="rdi light">7%</td></tr>
      <tr><td><b>Total Fat</b> <span class="light">11g</span></td><td class="rdi"></td></tr>
      <tr><td class="sub">Saturated Fat 10g</td><td class="rdi"></td></tr>
      <tr><td class="sub"><i>Trans</i> Fat 0g</td><td class="rdi"></td></tr>
      <tr><td><b>Cholesterol</b> <span class="light">0mg</span></td><td class="rdi"></td></tr>
      <tr><td><b>Sodium</b> <span class="light">117mg</span></td><td class="rdi"></td></tr>
      <tr><td><b>Total Carbohydrate</b> <span class="light">16g</span></td><td class="rdi"></td></tr>
      <tr><td class="sub">Dietary Fiber 4g</td><td class="rdi"></td></tr>
      <tr><td class="sub">Sugar 8g</td><td class="rdi"></td></tr>
      <tr><td><b>Protein</b> <span class="light">2g</span></td><td class="rdi light">2%</td></tr>
    </table>
    <p class="facts-note">*Percent RENI values are based on FNRI RENI 2002 reference male adult requirement of 19-29 years old</p>
  </section>

  <section class="ingredients">
    <h3 class="ingredients-title">INGREDIENTS:</h3>
    <p class="ingredients-list">Coconut Meat, Sugar, Salt and Sodium Metabisulfite</p>
  </section>
  <p class="net-weight">Net Weight 60g</p>
</main>
</body>
</html>
```